Business Card Design for Law firm - already have logo

Now that we have a logo, we need a business card design - our logo is attached -it is salaryman font if that helps - we would like a file that can be uploaded to cardquill (www.cardquill-example.com) using the logo and with the following information on it:
Quenby Law Firm, P.C.
Delwyn Quenby, Esq.
5817 SW 19th Ave.
Portland, OR 97213
971.555.0142 phone
971.555.0187 fax
del@quenby-example.net
Skype: delquenby
Google talk: delwyn.quenby@mailbox-example.com
Target Market(s)
our business cards are distributed to corporate executives, technology professionals and healthcare providers
Industry/Entity Type
Business
Look and feel

```html
<!DOCTYPE html>
<html lang="en">
<head>
<meta charset="utf-8">
<title>Quenby Law Firm – Business Card</title>
<link rel="stylesheet" href="https://fonts.googleapis.com/css2?family=Archivo+Black&family=Bebas+Neue&display=swap">
<style>
  :root {
    --page: #ffffff;
    --card: #333132;
    --ink-light: #ffffff;
    --band: #fec908;
    --ink-dark: #333132;
  }
  html, body {
    margin: 0;
    padding: 0;
    width: 1200px;
    height: 1000px;
    overflow: hidden;
    background: var(--page);
  }
  .card {
    position: absolute;
    left: 38px;
    top: 163px;
    width: 1125px;
    height: 675px;
    background: var(--card);
  }
  .wordmark {
    position: absolute;
    left: 165px;
    top: 135px;
    width: 807px;
    height: 195px;
    display: flex;
    align-items: center;
    justify-content: center;
    font-family: "Bebas Neue", sans-serif;
    font-size: 190px;
    letter-spacing: 48px;
    line-height: 1;
    color: var(--ink-light);
    padding-left: 48px;
    box-sizing: border-box;
  }
  .firm-name {
    position: absolute;
    left: 165px;
    top: 357px;
    margin: 0;
    font-family: "Bebas Neue", sans-serif;
    font-weight: 400;
    font-size: 66px;
    line-height: 1;
    color: var(--ink-light);
  }
  .attorney {
    position: absolute;
    left: 165px;
    top: 425px;
    margin: 0;
    font-family: "Bebas Neue", sans-serif;
    font-weight: 400;
    font-size: 42px;
    line-height: 1;
    color: var(--ink-light);
  }
  .band {
    position: absolute;
    left: 125px;
    width: 874px;
    height: 50px;
    border-radius: 18px;
    background: var(--band);
  }
  .band--top { top: 470px; }
  .band--bottom { top: 532px; }
  .badge {
    position: absolute;
    top: 0;
    width: 62px;
    height: 50px;
  }
  .contact {
    position: absolute;
    font-family: "Bebas Neue", sans-serif;
    font-size: 25px;
    line-height: 50px;
    top: 0;
    color: var(--ink-dark);
    white-space: nowrap;
  }
  .address {
    position: absolute;
    left: 549px;
    top: 5px;
    font-family: "Archivo Black", sans-serif;
    font-size: 17px;
    line-height: 22px;
    color: var(--ink-dark);
    text-transform: uppercase;
    letter-spacing: 0.5px;
  }
</style>
</head>
<body>
  <section class="card">
    <div class="wordmark">QUENBY</div>
    <h1 class="firm-name">QUENBY LAW FIRM, P.C.</h1>
    <h2 class="attorney">DELWYN QUENBY, ESQ.</h2>

    <div class="band band--top">
      <svg class="badge" style="left:20px" viewBox="0 0 62 50" aria-hidden="true">
        <polygon points="0,25 16,0 46,0 62,25 46,50 16,50" fill="var(--ink-dark)"/>
        <circle cx="31" cy="25" r="10" fill="none" stroke="#fff" stroke-width="2.5"/>
      </svg>
      <span class="contact" style="left:104px">DELWYN.QUENBY@MAILBOX-EXAMPLE.COM</span>

      <svg class="badge" style="left:462px" viewBox="0 0 62 50" aria-hidden="true">
        <polygon points="0,25 16,0 46,0 62,25 46,50 16,50" fill="var(--ink-dark)"/>
        <polygon points="31,9 16,23 20,23 20,38 28,38 28,30 34,30 34,38 42,38 42,23 46,23" fill="#eeeeee"/>
      </svg>
      <div class="address">5817 SW 19th Ave.<br>Portland, OR 97213</div>
    </div>

    <div class="band band--bottom">
      <svg class="badge" style="left:20px" viewBox="0 0 62 50" aria-hidden="true">
        <polygon points="0,25 16,0 46,0 62,25 46,50 16,50" fill="var(--ink-dark)"/>
        <rect x="21" y="8" width="20" height="34" rx="3" fill="#111"/>
        <rect x="23" y="11" width="16" height="24" fill="#fff"/>
        <circle cx="27" cy="38.5" r="1.2" fill="#fff"/>
        <circle cx="31" cy="38.5" r="1.2" fill="#fff"/>
        <circle cx="35" cy="38.5" r="1.2" fill="#fff"/>
      </svg>
      <span class="contact" style="left:98px">971.555.0142</span>

      <svg class="badge" style="left:237px" viewBox="0 0 62 50" aria-hidden="true">
        <polygon points="0,25 16,0 46,0 62,25 46,50 16,50" fill="var(--ink-dark)"/>
        <rect x="19" y="10" width="24" height="30" rx="3" fill="#111" stroke="#fff" stroke-width="2"/>
        <rect x="24" y="14" width="14" height="9" fill="#fff"/>
        <path d="M25 31 q6 -5 12 0 v3 h-12z" fill="#fff"/>
      </svg>
      <span class="contact" style="left:311px">971.555.0187</span>

      <svg class="badge" style="left:462px" viewBox="0 0 62 50" aria-hidden="true">
        <polygon points="0,25 16,0 46,0 62,25 46,50 16,50" fill="var(--ink-dark)"/>
        <circle cx="31" cy="25" r="11" fill="#eeeeee"/>
      </svg>
      <span class="contact" style="left:545px">DELQUENBY</span>
    </div>
  </section>
</body>
</html>
```